Brightmoor Partners Branding Revamp

We are a consulting company, looking for a way to display and promote our brand. We have 2 sides to the business- Brightmoor (financial) and Partners (cyber security). The financial side products relate to business necessities: card processing, website design/hosting/maintenance, VoIP phone systems. The cyber security side promotes a bundled package of 4 solutions: network vulnerability scan, dark web scan, anti-ransomeware/malware software, and image-level backups. We want people to understand that partnering with Brightmoor Partners gives them “Assured Calm for Business” (tagline). Current badge and logos uploaded.

Target Market(s)

Small businesses

Contact Information for Business Card

Lena Marwick, Vice President, lena@brightmoorpartners.example, 555-806-1937, www.brightmoorpartners.example

Requirements
Nice to have
• I do prefer the darker background for front and back

```html
<!DOCTYPE html>
<html lang="en">
<head>
<meta charset="utf-8">
<title>Brightmoor Partners — Business Card</title>
<link href="https://fonts.googleapis.com/css2?family=Michroma&family=Orbitron:wght@700&family=Montserrat:wght@400;500&display=swap" rel="stylesheet">
<style>
  :root {
    --page: #ffffff;
    --card: #000000;
    --ink: #ffffff;
    --accent: #e0222b;
    --accent-deep: #7a0a10;
    --rule: #8a8a8a;
  }
  * { box-sizing: border-box; margin: 0; padding: 0; }
  html, body { width: 686px; height: 1200px; overflow: hidden; background: var(--page); }
  .sheet { position: relative; width: 686px; height: 1200px; }

  .card {
    position: absolute; left: 43px; width: 600px; height: 343px;
    background: var(--card); overflow: hidden; color: var(--ink);
  }
  .card--front { top: 220px; }
  .card--back { top: 620px; }

  .corner-art { position: absolute; inset: 0; width: 100%; height: 100%; }

  .wordmark {
    font-family: "Michroma", sans-serif; color: var(--ink);
    text-transform: uppercase; text-align: center; line-height: 1.35;
  }
  .wordmark__mark {
    display: block; width: 26px; height: 26px; background: var(--accent);
    margin: 0 auto 16px;
  }

  .card--front .wordmark {
    position: absolute; top: 78px; left: 0; right: 0;
    font-size: 16px; letter-spacing: 4px;
  }
  .tagline {
    position: absolute; top: 212px; left: 0; right: 0; text-align: center;
    font-family: "Orbitron", sans-serif; font-weight: 700; font-size: 21px;
    letter-spacing: 0.5px; text-transform: uppercase; white-space: nowrap;
  }
  .front-url {
    position: absolute; top: 290px; left: 0; right: 0; text-align: center;
    font-family: "Montserrat", sans-serif; font-size: 12px; letter-spacing: 5px;
  }

  .card--back .wordmark {
    position: absolute; top: 130px; left: 20px; width: 256px;
    font-size: 15px; letter-spacing: 4px;
  }
  .divider {
    position: absolute; left: 274px; top: 124px; height: 132px;
    border-left: 1px dotted var(--rule);
  }
  .contact { position: absolute; left: 304px; top: 120px; font-family: "Montserrat", sans-serif; }
  .contact__name {
    font-family: "Orbitron", sans-serif; font-weight: 700; color: var(--accent);
    font-size: 19px; text-transform: uppercase; letter-spacing: 0.3px; white-space: nowrap;
  }
  .contact__title { font-size: 16px; margin-top: 2px; font-weight: 500; }
  .contact__list { list-style: none; margin-top: 18px; }
  .contact__item { display: flex; align-items: center; gap: 11px; font-size: 13px; height: 25px; white-space: nowrap; }
  .contact__icon { width: 18px; height: 18px; flex: none; }
</style>
</head>
<body>
<main class="sheet">

  <section class="card card--front" aria-label="Business card front">
    <svg class="corner-art" viewBox="0 0 600 343" role="img" aria-label="Red angled line pattern in the corners">
      <defs>
        <linearGradient id="frontTop" x1="1" y1="0" x2="0.35" y2="0.6">
          <stop offset="0" stop-color="#e0222b"/>
          <stop offset="0.55" stop-color="#5a060b"/>
          <stop offset="1" stop-color="#000" stop-opacity="0"/>
        </linearGradient>
        <linearGradient id="frontBottom" x1="0" y1="1" x2="0.6" y2="0.3">
          <stop offset="0" stop-color="#c41a22"/>
          <stop offset="1" stop-color="#000" stop-opacity="0"/>
        </linearGradient>
      </defs>
      <polygon points="330,0 600,0 600,228" fill="url(#frontTop)"/>
      <polygon points="0,255 0,343 115,343" fill="url(#frontBottom)"/>
    </svg>
    <div class="wordmark"><span class="wordmark__mark"></span>Brightmoor Partners</div>
    <p class="tagline">Assured Calm for Business</p>
    <p class="front-url">www.brightmoorpartners.example</p>
  </section>

  <section class="card card--back" aria-label="Business card back">
    <svg class="corner-art" viewBox="0 0 600 343" role="img" aria-label="Red angled line pattern in the corners">
      <defs>
        <linearGradient id="backTop" x1="0" y1="0" x2="0.55" y2="0.6">
          <stop offset="0" stop-color="#e0222b"/>
          <stop offset="0.5" stop-color="#5a060b"/>
          <stop offset="1" stop-color="#000" stop-opacity="0"/>
        </linearGradient>
        <linearGradient id="backBottom" x1="1" y1="1" x2="0.4" y2="0.3">
          <stop offset="0" stop-color="#c41a22"/>
          <stop offset="1" stop-color="#000" stop-opacity="0"/>
        </linearGradient>
      </defs>
      <polygon points="0,0 170,0 0,125" fill="url(#backTop)"/>
      <polygon points="600,265 600,343 490,343" fill="url(#backBottom)"/>
    </svg>

    <div class="wordmark"><span class="wordmark__mark"></span>Brightmoor<br>Partners</div>
    <div class="divider"></div>

    <div class="contact">
      <h1 class="contact__name">Lena Marwick</h1>
      <p class="contact__title">Vice President</p>
      <ul class="contact__list">
        <li class="contact__item">
          <svg class="contact__icon" viewBox="0 0 18 18" aria-hidden="true"><circle cx="9" cy="9" r="9" fill="var(--accent)"/><path d="M6 5.2l1.6-.4 1 2.2-1 .8a5 5 0 0 0 2.6 2.6l.8-1 2.2 1-.4 1.6c-3.7.3-7.1-3.1-6.8-6.8z" fill="#fff"/></svg>
          555-806-1937
        </li>
        <li class="contact__item">
          <svg class="contact__icon" viewBox="0 0 18 18" aria-hidden="true"><circle cx="9" cy="9" r="9" fill="var(--accent)"/><rect x="5" y="6" width="8" height="6" fill="#fff"/><path d="M5 6l4 3.2L13 6" stroke="var(--accent)" stroke-width="1" fill="none"/></svg>
          lena@brightmoorpartners.example
        </li>
        <li class="contact__item">
          <svg class="contact__icon" viewBox="0 0 18 18" aria-hidden="true"><circle cx="9" cy="9" r="9" fill="var(--accent)"/><g stroke="#fff" stroke-width="0.9" fill="none"><circle cx="9" cy="9" r="4.2"/><ellipse cx="9" cy="9" rx="1.8" ry="4.2"/><path d="M4.8 9h8.4"/></g></svg>
          www.brightmoorpartners.example
        </li>
      </ul>
    </div>
  </section>

</main>
</body>
</html>
```